5 Planner Covers for Teacher Planners

Hello,
I currently run a Speech-Language Pathologist website and have created a planner for my fellow Speech Therapist. I would like someone to create 5 different planner covers so my followers will have different options to choose from.
Here is my planner from last year to give you an idea of what the planner will look like http://www.talkwellnook.example/free-slp-planner/
My followers are mostly women aged 25-50. However, I don't want the covers to be overly girly or excessive with flowers. Simple is better.
I'd also like there to be an editable text box to allow the Speech Therapist to type their name on their cover if they wish.
Planner Cover can say any of the following: SLP Planner, Planner, Speech Therapy Planner, Speech-Language Pathologist (maybe this title could be editable as well??).
To give you an idea I have uploaded a screenshot of last year's planners cover that I made myself.
What I am looking for:
-Size 8.5" by 11"
-5 different planner covers
-1 gender-neutral cover
-simple design
-limited flowers (or overly girly
-text box to add a personal name
-Possible titles: SLP Planner, Planner, Speech Therapy Planner, Speech-Language Pathologist (maybe this title could be editable as well??)
Target Market(s)
Women aged 25-50
Colors
Designer to choose colors to be used in the design.
Requirements
Must have
- What I am looking for:
-Size 8.5" by 11"
-1 gender-neutral cover
-simple design
Nice to have
- I've uploaded some that I like from Craftly to give you an idea.
Here is my craftly store https://www.craftly.example/shop/QuietMeadowHome to give you an idea of things I like.
I like Marla Hensley and her simple elegant rustic style.

```html
<!DOCTYPE html>
<html lang="en">
<head>
<meta charset="utf-8">
<title>SLP Planner Cover</title>
<link rel="stylesheet" href="https://fonts.googleapis.com/css2?family=Allura&display=swap">
<style>
  :root {
    --violet-deep: #4a1f7a;
    --violet-mid: #7a3aa8;
    --orchid: #a955c4;
    --plum: #6b2a7e;
    --lilac: #b98ad8;
    --label-ink: #ffffff;
  }
  * { margin: 0; padding: 0; box-sizing: border-box; }
  html, body { width: 927px; height: 1200px; overflow: hidden; }
  .planner-cover {
    position: relative;
    width: 927px;
    height: 1200px;
    overflow: hidden;
  }
  .cover-pattern {
    position: absolute;
    inset: 0;
    background:
      radial-gradient(circle at 20% 15%, var(--orchid) 0%, transparent 45%),
      radial-gradient(circle at 80% 70%, var(--lilac) 0%, transparent 40%),
      radial-gradient(circle at 70% 20%, var(--plum) 0%, transparent 45%),
      radial-gradient(circle at 25% 85%, var(--violet-mid) 0%, transparent 50%),
      linear-gradient(160deg, var(--violet-mid), var(--violet-deep) 55%, var(--orchid));
  }
  .name-label {
    position: absolute;
    inset: 0;
    width: 927px;
    height: 1200px;
  }
  .label-frame { fill: none; stroke: var(--label-ink); }
  .label-frame--outer { stroke-width: 5; }
  .label-frame--inner { stroke-width: 3; }
  .name-line { stroke: var(--label-ink); stroke-width: 2; }
  .label-title {
    font-family: "Allura", cursive;
    font-size: 66px;
    fill: var(--label-ink);
  }
  .label-subtitle {
    font-family: "Allura", cursive;
    font-size: 24px;
    fill: var(--label-ink);
  }
</style>
</head>
<body>
  <main class="planner-cover">
    <div class="cover-pattern" role="img" aria-label="Purple and violet low-poly geometric triangle pattern"></div>
    <svg class="name-label" viewBox="0 0 927 1200" xmlns="http://www.w3.org/2000/svg">
      <path class="label-frame label-frame--outer"
        d="M274 484 H654 A34 34 0 0 0 688 518 Q716 594 688 669 A34 34 0 0 0 654 703 H274 A34 34 0 0 0 240 669 Q212 594 240 518 A34 34 0 0 0 274 484 Z"/>
      <path class="label-frame label-frame--inner"
        d="M280 496 H648 A28 28 0 0 0 676 524 Q702 594 676 663 A28 28 0 0 0 648 691 H280 A28 28 0 0 0 252 663 Q226 594 252 524 A28 28 0 0 0 280 496 Z"/>
      <text class="label-title" x="452" y="572" text-anchor="middle">SLP Planner</text>
      <text class="label-subtitle" x="440" y="610" text-anchor="middle">belongs to</text>
      <line class="name-line" x1="332" y1="663" x2="569" y2="663"/>
    </svg>
  </main>
</body>
</html>
```